Yarnful Hours planner/ book cover

YARNFUL HOURS" - A UNIQUE NOTEBOOK FOR CRAFTS. The main goal of a "Yarnful Hours" notebook is to arrange your crafts notes like knitting planner. Its pages are systematically structured, so they are easy to review, and all the information about the started project is in one place. The notebook has a click opening system, so you can remove, insert, change pages.
This is the old design in Latvian language. I want a new, classic, modern cover design for selling book in USA.I prefer original picture rather than download. Maybe for some of yourself drawings. Illustrated color-wash and minimalistic style better than photography.
Look at the pages inside design so that the lid fits. Maybe i want to change some clipart on the inside as well (just small one, like ball of yarn, sweater, can be seen in the picture, more classic style, not so childish, but that's latter), leave yoga clipart and the colors. Check please video.
https://www.vidhollow.example/watch?v=Qm4tLr8wZ2k
www.yarnfulhours.example its my style.

book title- yarnful hours
slogan- its time for sitting to do some knitting
size- 18 x 23,5 x 4 cm

Colors
d3a5cc
eea4c8
fdf2f7
fbd4d5
fdf0f6
ffffff
e34297
a64599
b868aa

```html
<!DOCTYPE html>
<html lang="en">
<head>
<meta charset="utf-8">
<title>Yarnful Hours — Cover</title>
<link rel="stylesheet" href="https://fonts.googleapis.com/css2?family=Cormorant+Garamond:ital,wght@1,500&family=Roboto+Condensed:ital,wght@0,700;1,400&display=swap">
<style>
  :root {
    --frame-grey: #d9d9d9;
    --cover-brown: #9e7244;
    --paper: #ffffff;
    --ink: #3a3b3d;
    --title-white: #ffffff;
    --wool-light: #f2d08a;
    --wool-mid: #dcae5c;
    --wool-deep: #a9773a;
  }
  * { margin: 0; padding: 0; box-sizing: border-box; }
  html, body {
    width: 942px;
    height: 1200px;
    overflow: hidden;
    background: var(--frame-grey);
  }
  .cover {
    position: relative;
    width: 942px;
    height: 1200px;
    background: var(--frame-grey);
  }
  .cover-bands {
    position: absolute;
    inset: 0;
    width: 942px;
    height: 1200px;
  }
  .cover-bands .paper { fill: var(--paper); }
  .cover-bands .band { fill: var(--cover-brown); }
  .title {
    position: absolute;
    left: 33px;
    width: 876px;
    top: 78px;
    text-align: center;
    font-family: "Cormorant Garamond", serif;
    font-style: italic;
    font-weight: 500;
    font-size: 124px;
    line-height: 1;
    letter-spacing: 1px;
    color: var(--title-white);
  }
  .slogan {
    position: absolute;
    left: 33px;
    width: 876px;
    top: 384px;
    text-align: center;
    font-family: "Roboto Condensed", sans-serif;
    font-style: italic;
    font-weight: 400;
    font-size: 45px;
    line-height: 59px;
    color: var(--ink);
  }
  .knitting-illustration {
    position: absolute;
    left: 212px;
    top: 620px;
    width: 520px;
    height: 312px;
    border-radius: 30px 30px 60px 60px;
    background: radial-gradient(ellipse at 50% 40%, var(--wool-light) 0%, var(--wool-mid) 60%, var(--wool-deep) 100%);
    opacity: 0.85;
  }
  .imprint {
    position: absolute;
    left: 33px;
    width: 876px;
    top: 1080px;
    text-align: center;
    font-family: "Roboto Condensed", sans-serif;
    font-weight: 700;
    font-size: 36px;
    letter-spacing: 1px;
    color: var(--title-white);
  }
</style>
</head>
<body>
<main class="cover">
  <svg class="cover-bands" viewBox="0 0 1708 2183" preserveAspectRatio="none" aria-hidden="true">
    <rect class="paper" x="60" y="60" width="1586" height="2050"/>
    <polygon class="band" points="60,60 1646,60 1646,513 1418,598 1228,521 1040,598 852,521 668,598 476,521 292,598 60,520"/>
    <polygon class="band" points="62,1907 291,1822 483,1898 668,1822 856,1898 1040,1822 1231,1898 1418,1822 1646,1898 1646,2112 62,2112"/>
  </svg>

  <h1 class="title">yarnful hours</h1>

  <p class="slogan">its time for sitting to do<br>some knitting</p>

  <div class="knitting-illustration" role="img" aria-label="Watercolour illustration of a golden knitted piece on two crossed knitting needles"></div>

  <p class="imprint">STITCHWELL</p>
</main>
</body>
</html>
```